Singer/Songwriter Artist Promotion Website

***DO NOT CONTACT ME PRIVATELY***

I need a fresh, exciting, upbeat-looking site. The purpose of our business is to genuinely promote unknown, unsigned music artists. The sight initially needs a feel slanted toward Country Music.

DESIGN
The website design should be similar to this site;
https://www.pelvarotune.com

For the design, make it follow a linear flow of sections/blocks. We don't want a complex design with objects/images in random parts of the page, but rather section "blocks" of content.

I need 5 pages designed;
Home
FAQ
Our Staff
"Launch Your Music" This page is more complex. This page needs to display a questionnaire that can be filled out. This page will need to be able to capture and process payments. There needs to be a way to attach files for upload.
"Artist Profiles" - > A template page that will be used for multiple artists. It will show the artist/musician information

Design/Colors
I want colors that are attractive, professional but exciting. I’m looking for tasteful, interesting, eye-catching, not boring.

Taglines;
Name: “Bluefield Tunecast Circle”
Tagline: “All Original Artists-All Original Country
24/7, Commercial Free, All The Time”

LOGO DESIGN
- See attached basic logo
Bluefield Tunecast Circle
BTC
Base design off of attached logo. I’d like the "Bluefield Tunecast Circle" to be Colorful. Attention getting. Possibly showing some movement. Maybe a gradient.

Target Market(s)

Independent Musicians

Industry/Entity Type

Songwriting, Music Promotion, Radio Network

Number of Pages Required

5+ page

Colors
00AB8E
00BBA5
67D7C9
C6EFE9
E9F9F6

```html
<!DOCTYPE html>
<html lang="en">
<head>
<meta charset="utf-8">
<title>Bluefield Tunecast Circle</title>
<link rel="stylesheet" href="https://fonts.googleapis.com/css2?family=Lato:wght@400;700;900&family=Arimo:wght@400;700&family=Poppins:wght@400&display=swap">
<style>
  :root {
    --teal: #00AB8E;
    --teal-bright: #00BBA5;
    --teal-soft: #67D7C9;
    --teal-pale: #C6EFE9;
    --teal-mist: #E9F9F6;
    --ink: #222222;
    --body: #555555;
    --muted: #6b6b6b;
    --white: #ffffff;
    --grey-band: #f6f6f6;
    --dark-band: #2a2522;
  }
  * { box-sizing: border-box; margin: 0; padding: 0; }
  html, body { width: 1200px; height: 3948px; overflow: hidden; background: var(--white); }
  body { position: relative; font-family: "Arimo", Arial, sans-serif; color: var(--body); }
  a { color: inherit; text-decoration: none; }
  .heading { font-family: "Lato", sans-serif; font-weight: 700; color: var(--ink); }
  .rule { display: block; height: 3px; width: 106px; background: var(--teal); }
  .read-more { font-family: "Lato", sans-serif; font-size: 16px; color: var(--teal); text-decoration: underline; }

  /* header */
  .site-header { position: absolute; top: 0; left: 0; width: 1200px; height: 72px; background: var(--white); }
  .brand { position: absolute; left: 110px; top: 10px; display: flex; align-items: center; gap: 10px;
    font-family: "Lato", sans-serif; font-weight: 900; font-size: 46px; color: var(--teal); letter-spacing: 2px; line-height: 52px; }
  .brand-dot { width: 14px; height: 14px; background: var(--teal-soft); }
  .main-nav { position: absolute; right: 112px; top: 27px; display: flex; gap: 38px; font-size: 15px; color: var(--ink); }
  .main-nav .active { color: var(--teal); }

  /* hero */
  .hero { position: absolute; top: 72px; left: 0; width: 1200px; height: 644px; text-align: center; }
  .hero-photo { position: absolute; inset: 0;
    background: radial-gradient(ellipse at 62% 35%, #cbb9a8 0%, #9c8672 35%, #5d5146 70%, #3f3a33 100%); }
  .hero-shade { position: absolute; inset: 0; background: rgba(30,25,20,0.35); }
  .play { position: absolute; left: 560px; top: 211px; width: 82px; height: 82px; border-radius: 50%; background: var(--teal); }
  .hero-name { position: absolute; top: 312px; width: 100%; font-family: "Lato", sans-serif; font-weight: 700; font-size: 24px; color: var(--white); }
  .hero-tagline { position: absolute; top: 360px; width: 100%; font-family: "Lato", sans-serif; font-weight: 700; font-size: 33px; line-height: 49px; color: var(--white); }

  /* radio time */
  .radio-time { position: absolute; top: 716px; left: 0; width: 1200px; height: 599px; background: var(--white); }
  .radio-time .heading { position: absolute; left: 110px; top: 117px; font-size: 32px; line-height: 40px; }
  .radio-time .rule { position: absolute; left: 110px; top: 219px; }
  .checklist { position: absolute; left: 110px; top: 254px; list-style: none; font-size: 13px; color: var(--ink); }
  .checklist li { position: relative; padding-left: 27px; line-height: 33.5px; width: 490px; }
  .checklist li::before { content: "\2192"; position: absolute; left: 0; color: var(--teal); font-weight: 700; }
  .radio-photo { position: absolute; left: 641px; top: 55px; width: 444px; height: 492px; border-radius: 60px;
    background: linear-gradient(160deg, #e8e6e3 0%, #c9c2b9 45%, #6f7280 75%, #b7a892 100%); }

  /* answer band */
  .answer { position: absolute; top: 1315px; left: 0; width: 1200px; height: 513px; text-align: center; }
  .answer-photo { position: absolute; inset: 0; background: linear-gradient(180deg, #3a332e 0%, #2b2622 50%, #1e1b19 100%); }
  .answer .heading { position: absolute; top: 112px; width: 100%; font-size: 33px; line-height: 40px; color: var(--white); }
  .answer .rule { position: absolute; top: 217px; left: 547px; }
  .answer-copy { position: absolute; top: 240px; left: 175px; width: 850px; font-size: 13px; line-height: 27.5px; color: var(--white); }
  .answer-copy p + p { margin-top: 11px; }

  /* exposure */
  .exposure { position: absolute; top: 1828px; left: 0; width: 1200px; height: 744px; }
  .exposure .heading { position: absolute; top: 60px; width: 100%; text-align: center; font-size: 33px; line-height: 40px; }
  .exposure .rule { position: absolute; top: 160px; left: 547px; }
  .cards { position: absolute; top: 203px; left: 110px; display: flex; gap: 12px; }
  .card { width: 318px; }
  .card-photo { height: 272px; border-radius: 18px; }
  .card-photo.writer { background: linear-gradient(150deg, #8a8983 0%, #c9c3b8 50%, #6d6a65 100%); }
  .card-photo.studio { background: linear-gradient(150deg, #d8d6d3 0%, #f0efed 45%, #54504c 100%); }
  .card-photo.laptop { background: linear-gradient(150deg, #e9e6e0 0%, #b98a5c 50%, #5a4a3d 100%); }
  .card-title { font-family: "Lato", sans-serif; font-weight: 700; font-size: 24px; color: var(--ink); margin-top: 17px; line-height: 30px; }
  .card-text { margin-top: 6px; font-size: 12.5px; line-height: 26px; color: var(--ink); height: 110px; }
  .card .read-more { display: inline-block; margin-top: 12px; }

  /* cost & start */
  .cost-start { position: absolute; top: 2572px; left: 0; width: 1200px; height: 1168px; background: var(--grey-band); }
  .cost-photo { position: absolute; left: 110px; top: 82px; width: 443px; height: 492px; border-radius: 60px;
    background: linear-gradient(160deg, #a8a090 0%, #8a7760 45%, #4f4336 100%); }
  .cost { position: absolute; left: 604px; top: 150px; width: 480px; }
  .cost .heading, .start .heading { font-size: 32px; line-height: 40px; }
  .cost .rule, .start .rule { margin-top: 10px; }
  .lead { margin-top: 17px; font-family: "Lato", sans-serif; font-size: 14px; line-height: 25px; color: var(--ink); }
  .copy { margin-top: 12px; font-size: 12.5px; line-height: 26px; color: var(--muted); }
  .cost .read-more, .start .read-more { display: inline-block; margin-top: 12px; }
  .start { position: absolute; left: 110px; top: 717px; width: 480px; }
  .start .copy p + p { margin-top: 8px; }
  .start-photo { position: absolute; left: 644px; top: 622px; width: 441px; height: 490px; border-radius: 60px;
    background: linear-gradient(160deg, #6f6a64 0%, #c8c4bf 50%, #f2f1ef 100%); }

  /* footer */
  .site-footer { position: absolute; top: 3740px; left: 0; width: 1200px; height: 208px; background: var(--teal); text-align: center; color: var(--white); }
  .footer-nav { position: absolute; top: 46px; width: 100%; display: flex; justify-content: center; gap: 30px; font-size: 15px; }
  .social { position: absolute; top: 110px; width: 100%; display: flex; justify-content: center; gap: 12px; }
  .social span { width: 40px; height: 40px; border: 1.5px solid var(--white); border-radius: 50%; }
  .copyright { position: absolute; top: 156px; width: 100%; font-family: "Poppins", sans-serif; font-size: 14px; }
</style>
</head>
<body>

<header class="site-header">
  <a class="brand" href="#"><span>BTC</span><span class="brand-dot"></span></a>
  <nav class="main-nav">
    <a class="active" href="#">Home</a>
    <a href="#">About Us</a>
    <a href="#">How It Works?</a>
    <a href="#">FAQ</a>
    <a href="#">Contact</a>
  </nav>
</header>

<section class="hero">
  <div class="hero-photo" role="img" aria-label="Young woman writing a song in a notebook while holding a ukulele"></div>
  <div class="hero-shade"></div>
  <span class="play">
    <svg width="82" height="82" viewBox="0 0 82 82"><polygon points="33,27 33,55 56,41" fill="#ffffff"/></svg>
  </span>
  <p class="hero-name">Bluefield Tunecast Circle</p>
  <h1 class="hero-tagline">All Original Artists-All Original Country 24/7,<br>Commercial Free, All The Time</h1>
</section>

<section class="radio-time">
  <h2 class="heading">How much radio time did you<br>get last month?</h2>
  <span class="rule"></span>
  <ul class="checklist">
    <li>Are you a compelling singer/songwriter?</li>
    <li>Have you written some really strong country songs that you feel could rival the big artists?</li>
    <li>Do you want to expand your fan base?</li>
    <li>Do you have CDs, LPs or downloads to sell?</li>
    <li>Would you be okay with international exposure?</li>
    <li>Are you frustrated trying to get the exposure you deserve?</li>
  </ul>
  <div class="radio-photo" role="img" aria-label="Man in a beanie writing lyrics on a chair beside a guitar"></div>
</section>

<section class="answer">
  <div class="answer-photo" role="img" aria-label="Dim photo of sheet music on a piano"></div>
  <h2 class="heading">Bluefield Tunecast Circle<br>has the answer!</h2>
  <span class="rule"></span>
  <div class="answer-copy">
    <p>In the 1990’s, the music industry imploded with the closing of large recording studios. At the same time, with the dawning of digital home studios, the number of solid songwriting artists exploded. It is now easier than ever for talented artists to record and release their music but who is listening and how can you reach the masses with to your music?</p>
    <p>We are US based company with DJs based in Australia, Scotland, Germany, England, USA and beyond. Our network of international DJ’s offer original songwriting artists a worldwide platform to showcase their songs.</p>
  </div>
</section>

<section class="exposure">
  <h2 class="heading">Get over 4 1/2 hours of exposure<br>per month.</h2>
  <span class="rule"></span>
  <div class="cards">
    <article class="card">
      <div class="card-photo writer" role="img" aria-label="Woman with headphones writing in a notebook"></div>
      <h3 class="card-title">BTC</h3>
      <p class="card-text">BTC provide you and your songs with international exposure.<br>We are truly dedicated to getting your music out and your success.</p>
      <a class="read-more" href="#">Read More</a>
    </article>
    <article class="card">
      <div class="card-photo studio" role="img" aria-label="Musician with headphones reading sheet music on a screen"></div>
      <h3 class="card-title">Who qualifies for BTC?</h3>
      <p class="card-text">We accept only origional material.<br>(No covers accepted).<br>Only high quality recordings of country music.<br>Only unsigned artists.</p>
      <a class="read-more" href="#">Read More</a>
    </article>
    <article class="card">
      <div class="card-photo laptop" role="img" aria-label="Woman with headphones working on a laptop"></div>
      <h3 class="card-title">How it works?</h3>
      <p class="card-text">Submit 2 songs for review. If they are accepted, we want you to create an audiorecording of your voice, giving our listeners a quick background on yourself, a littleinfo about the songs and where people</p>
      <a class="read-more" href="#">Read More</a>
    </article>
  </div>
</section>

<section class="cost-start">
  <div class="cost-photo" role="img" aria-label="Band members writing songs together in a rehearsal room"></div>
  <div class="cost">
    <h2 class="heading">What is the cost?</h2>
    <span class="rule"></span>
    <p class="lead">Right now, for you, there’s NO COST! For a limited time,<br>this exposure is FREE!</p>
    <p class="copy">The Bluefield Tunecast Circle is being launched in September, 2022! During this inital launch, we are reaching out to a small number of artist friends and studio owner friends asking for referrals. Right now, we’re lining up enough talented singer/songwriters to build our first couple of 3-hour shows. Once all of the show slots are filled, we will begin to charge a fee for new artists who want to use our radio promotion. In the meantime, this offer is FREE for you. You are being given this offer because someone</p>
    <a class="read-more" href="#">Read More</a>
  </div>

  <div class="start">
    <h2 class="heading">How Do I Start?</h2>
    <div class="copy">
      <p>First, contact me directly through an email, phone, text or form below. I will send you a form to sign and a simple bio sheet asking some basic questions about you and your songs. This will help our DJs promote you and let listeners know where they can find you and purchase your music. (Marketbay, your website, etc).</p>
      <p>On the form you will sign will state that we have your permission to broadcast your song and that you confirm that your songs are origional. Simple.</p>
    </div>
    <a class="read-more" href="#">Read More</a>
  </div>
  <div class="start-photo" role="img" aria-label="Man in glasses writing music beside a keyboard"></div>
</section>

<footer class="site-footer">
  <nav class="footer-nav">
    <a href="#">Home</a>
    <a href="#">About Us</a>
    <a href="#">How It Works</a>
    <a href="#">FAQ</a>
    <a href="#">Contact Us</a>
  </nav>
  <div class="social" aria-label="Social links">
    <span></span><span></span><span></span><span></span><span></span>
  </div>
  <p class="copyright">© 2022 All Rights Reserved</p>
</footer>

</body>
</html>
```